Window Cleaning Business Card Design

We need a business card design for a window cleaning business with the following design needs:

A symmetrical arc (drawn cartoon like and not a real picture) with a squeegee from left to right across the centretop of the card with the word "RADIANT" in the clean white space of the arc in a large font. The background can be a mid to dark blue colour and we would like some diamond sparkles randomly scattered. Below the arc is "WINDOW CLEANING PROFESSIONALS" in a slightly smaller font.

The "Call Brent or Lorna" can be in a flowing but not too busy font

Then the rest of the information in a business like font

Industry/Entity Type

Window Cleaning

Contact Information for Business Card

RADIANT
WINDOW CLEANING PROFESSIONALS
Call Brent or Lorna
0417 593 610
52 37 4418
radiantwindowcleaning@qarvel.com

(Then in bullet form pls put the following info)

Reliable, Friendly and Professional
Free Quotes - Affordable Rates
Fully Insured
Locally Owned and Operated
Quality Work with over 10yrs Experience

```html
<!DOCTYPE html>
<html lang="en">
<head>
<meta charset="utf-8">
<title>Radiant Window Cleaning – Business Card</title>
<link rel="stylesheet" href="https://fonts.googleapis.com/css2?family=Arimo:wght@400;700&family=Questrial&family=Roboto+Condensed:ital,wght@0,400;1,400&display=swap">
<style>
  :root {
    --page-bg: #f0f0f0;
    --card-light: #55b0c6;
    --card-dark: #0a93ad;
    --ink: #ffffff;
    --sparkle-area: rgba(255, 255, 255, 0.28);
  }
  html, body {
    margin: 0;
    width: 1200px;
    height: 1000px;
    overflow: hidden;
    background: var(--page-bg);
  }
  .business-card {
    position: absolute;
    left: 162px;
    top: 230px;
    width: 877px;
    height: 541px;
    background: linear-gradient(100deg, var(--card-light) 0%, #2fa2bb 55%, var(--card-dark) 100%);
    color: var(--ink);
    font-family: "Arimo", Arial, sans-serif;
  }
  .brand-square {
    position: absolute;
    left: 56px;
    top: 55px;
    width: 118px;
    height: 118px;
    background: var(--ink);
  }
  .brand-name {
    position: absolute;
    left: 198px;
    top: 50px;
    margin: 0;
    font-family: "Arimo", Arial, sans-serif;
    font-weight: 700;
    font-size: 86px;
    line-height: 1;
    letter-spacing: 1px;
  }
  .tagline {
    position: absolute;
    left: 200px;
    top: 139px;
    margin: 0;
    font-family: "Roboto Condensed", "Arial Narrow", sans-serif;
    font-size: 24px;
    letter-spacing: 0.9px;
    word-spacing: 6px;
    line-height: 1;
  }
  .sparkle-area {
    position: absolute;
    left: 622px;
    top: 146px;
    width: 190px;
    height: 185px;
    border-radius: 50%;
    background: radial-gradient(circle, var(--sparkle-area) 0%, rgba(255,255,255,0) 70%);
  }
  .phone-icon {
    position: absolute;
    left: 56px;
    top: 239px;
    width: 56px;
    height: 56px;
  }
  .contact-call {
    position: absolute;
    left: 130px;
    top: 226px;
    margin: 0;
    font-family: "Questrial", "Century Gothic", sans-serif;
    font-size: 34px;
    line-height: 41px;
  }
  .contact-call span { display: block; }
  .features {
    position: absolute;
    left: 56px;
    top: 336px;
    margin: 0;
    padding: 0;
    list-style: none;
    font-size: 24.5px;
    line-height: 31.5px;
  }
  .features li::before { content: "• "; }
  .email {
    position: absolute;
    left: 57px;
    top: 466px;
    margin: 0;
    font-family: "Roboto Condensed", "Arial Narrow", sans-serif;
    font-style: italic;
    font-size: 32px;
    line-height: 1;
  }
</style>
</head>
<body>
  <main class="business-card">
    <div class="brand-square"></div>
    <h1 class="brand-name">RADIANT</h1>
    <p class="tagline">WINDOW CLEANING PROFESSIONALS</p>

    <div class="sparkle-area" role="img" aria-label="Two soft sparkle shapes as decoration"></div>

    <svg class="phone-icon" viewBox="0 0 56 56" aria-hidden="true">
      <circle cx="28" cy="28" r="25.5" fill="none" stroke="#fff" stroke-width="3.5"/>
      <path fill="#fff" d="M18.5 14.5c1.2-.9 2.7-.6 3.5.6l3 4.6c.7 1.1.5 2.5-.5 3.3l-2 1.6c1.3 3.4 4 6.4 7.4 8l1.7-1.9c.9-1 2.3-1.1 3.3-.4l4.5 3.2c1.1.8 1.4 2.4.5 3.5l-1.8 2.3c-1.3 1.6-3.6 2.1-5.6 1.3-7.7-3.1-13.4-9.5-15.7-17.4-.6-2 .2-4.1 1.9-5.3z"/>
    </svg>
    <p class="contact-call">
      <span>Call Brent or Lorna</span>
      <span>0417 593 610 52 37 4418</span>
    </p>

    <ul class="features">
      <li>Reliable, Friendly and Professional Free Quotes</li>
      <li>Affordable Rates Fully Insured Locally Owned</li>
      <li>Operated Quality Work with over 10yrs Experience</li>
    </ul>

    <p class="email">radiantwindowcleaning@qarvel.com</p>
  </main>
</body>
</html>
```